integrative health clinic-Medical massage, acupuncture, chiropractic

we like our logo, but are open to new ideas. We need a new card design. We have added chiropractic and acupuncture that we have put under the name of the business. We are an integrative medical clinic

Target Market(s)

General public, athletes

Contact Information for Business Card

Phone 5055582917
Fax 5055582916
Hours Monday-Friday 9-6
Saturday 10-6
The 20% can be smaller on the back

Colors
3176b5
0355a3

Requirements
Must have
• Logo but am open to ideas
Nice to have
• We are an integrated medical clinic but also want to be personable. We want the card fun and inviting

```html
<!DOCTYPE html>
<html lang="en">
<head>
<meta charset="utf-8">
<title>Summit Body Wellness – Business Card</title>
<link rel="stylesheet" href="https://fonts.googleapis.com/css2?family=Open+Sans:wght@400;600;700&family=EB+Garamond:ital@1&display=swap">
<style>
  :root {
    --backdrop: #e4e4e6;
    --card: #f7f7f7;
    --ink: #1a1a1a;
    --brand-blue: #283b91;
    --band-grey: #c3c4c6;
  }
  * { margin: 0; padding: 0; box-sizing: border-box; }
  html, body { width: 1200px; height: 1021px; overflow: hidden; }
  body {
    background: var(--backdrop);
    font-family: "Open Sans", sans-serif;
    color: var(--ink);
    display: flex;
    flex-direction: column;
    align-items: center;
    justify-content: center;
    gap: 48px;
  }
  .card {
    position: relative;
    width: 760px;
    height: 434px;
    background: var(--card);
    box-shadow: 0 6px 18px rgba(0,0,0,.18);
    overflow: hidden;
  }

  /* Back side */
  .card-back { display: flex; align-items: center; justify-content: space-between; padding: 0 60px; }
  .booking { display: flex; flex-direction: column; gap: 14px; }
  .booking-title { color: var(--brand-blue); font-weight: 600; font-size: 34px; line-height: 1; }
  .booking-url { color: var(--brand-blue); font-weight: 600; font-size: 16px; }
  .offer { color: var(--brand-blue); text-align: center; font-weight: 700; line-height: .95; }
  .offer-amount { font-size: 68px; }
  .offer-amount small { font-size: 40px; }
  .offer-note { font-size: 30px; }
  .coverage { display: flex; flex-direction: column; align-items: flex-start; gap: 18px; width: 210px; }
  .coverage-text { font-size: 16px; line-height: 1.3; }
  .social-square { width: 30px; height: 30px; border-radius: 5px; background: var(--brand-blue); }

  /* Front side */
  .swoosh { position: absolute; inset: 0; }
  .front-content { position: absolute; left: 56px; top: 48px; }
  .brand { display: flex; align-items: center; gap: 12px; }
  .brand-dot { width: 30px; height: 30px; border-radius: 50%; background: var(--brand-blue); }
  .brand-name { font-size: 40px; font-weight: 600; letter-spacing: -.5px; color: var(--ink); }
  .brand-tagline { font-family: "EB Garamond", serif; font-style: italic; font-size: 21px; margin: 2px 0 0 58px; }
  .services { margin: 20px 0 0 40px; font-size: 21px; line-height: 1.3; }
  .contact { list-style: none; margin-top: 30px; font-size: 20px; line-height: 1.4; }
  .contact li { display: flex; align-items: center; gap: 10px; }
  .contact svg { width: 18px; height: 18px; fill: var(--brand-blue); flex: none; }
  .contact .address { padding-left: 0; }
</style>
</head>
<body>

<section class="card card-back">
  <div class="booking">
    <p class="booking-title">Book Online</p>
    <p class="booking-url">www.summitbodywellnessnm.com</p>
  </div>
  <div class="offer">
    <p class="offer-amount">20<small>%</small> OFF</p>
    <p class="offer-note">FIRST VISIT</p>
  </div>
  <div class="coverage">
    <p class="coverage-text">We accept some insurances, Worker's Comp and Personal Injury.</p>
    <span class="social-square" aria-label="Social page"></span>
  </div>
</section>

<section class="card card-front">
  <svg class="swoosh" viewBox="0 0 760 434" preserveAspectRatio="none" aria-hidden="true">
    <path d="M455 434 C610 400 700 240 680 70 L760 48 L760 434 Z" fill="var(--band-grey)"/>
    <path d="M505 434 C650 395 735 245 720 55 L760 45 L760 434 Z" fill="var(--brand-blue)"/>
  </svg>
  <div class="front-content">
    <div class="brand">
      <span class="brand-dot"></span>
      <span class="brand-name">Summit Body Wellness</span>
    </div>
    <p class="brand-tagline">Sports Therapy and Wellness Center</p>
    <p class="services">Specializing in<br>Medical, Sports Massage<br>Chiropractic and Acupuncture</p>
    <ul class="contact">
      <li><svg viewBox="0 0 24 24"><path d="M6.6 10.8a15.1 15.1 0 0 0 6.6 6.6l2.2-2.2c.3-.3.7-.4 1-.2 1.1.4 2.3.6 3.6.6.6 0 1 .4 1 1V20c0 .6-.4 1-1 1A17 17 0 0 1 3 4c0-.6.4-1 1-1h3.5c.6 0 1 .4 1 1 0 1.3.2 2.5.6 3.6.1.3 0 .7-.2 1z"/></svg>(505) 558-2917</li>
      <li><svg viewBox="0 0 24 24"><path d="M2 5h20v14H2zm2 2v.4l8 5.3 8-5.3V7zm0 2.8V17h16V9.8l-8 5.3z"/></svg>hello@summitbodywellnessnm.com</li>
      <li class="address">1480 Mesa Verde Rd, Suite 4, Santa Fe, NM 87505</li>
    </ul>
  </div>
</section>

</body>
</html>
```